need a clean, modern job advertisement designed for social media (Facebook & Instagram).

The post is to advertise two positions:
• Leading Hand Boilermaker
• Dragline Fitter
We want the design to match our KRT Plant Services branding: blue, white, strong, professional, mining-industry style.
What the design should include:
Bold headline: “WE’RE HIRING”
Sub-headline: “Leading Hand Boilermaker & Dragline Fitter”
Key points:
• Bowen Basin based
• Dragline & shovel maintenance
• Great pay + long-term work
• Locally owned & operated
KRT logo placed cleanly
Space for 1–2 images (boilermaking or dragline work)
Design style:
Strong and industrial
Blue/white colour scheme
Easy to read at a glance
Suitable for a square 1080×1080 design

```html
<!DOCTYPE html>
<html lang="en">
<head>
<meta charset="utf-8">
<title>KRT Plant Services – We're Hiring social posts</title>
<link rel="stylesheet" href="https://fonts.googleapis.com/css2?family=Open+Sans:ital,wght@0,400;0,600;0,700;0,800;1,400;1,600;1,700;1,800&display=swap">
<style>
  :root{
    --sheet:#e3e3e3;
    --black:#050505;
    --ink:#111418;
    --white:#ffffff;
    --blue:#0a6cff;
    --blue-deep:#0a4dff;
    --cyan:#12d6ff;
    --sky:#1aa3ff;
    --steel:#3a4654;
  }
  *{box-sizing:border-box;margin:0;padding:0}
  html,body{width:1192px;height:1200px;overflow:hidden}
  body{background:var(--sheet);position:relative;font-family:"Open Sans",Arial,sans-serif}
  .post{position:absolute;width:458px;height:458px;overflow:hidden;box-shadow:2px 3px 6px rgba(0,0,0,.35)}
  .post--a{left:129px;top:126px;background:var(--black)}
  .post--b{left:614px;top:126px;background:var(--white)}
  .post--c{left:129px;top:621px;background:var(--blue)}
  .post--d{left:614px;top:621px;background:#1b1d20}
  .abs{position:absolute}
  .headline{font-weight:800;font-style:italic;line-height:1;letter-spacing:-1px;white-space:nowrap}
  .accent{background:linear-gradient(90deg,var(--blue) 0%,var(--cyan) 100%);-webkit-background-clip:text;background-clip:text;color:transparent}
  .bold-it{font-weight:800;font-style:italic;line-height:1.05;white-space:nowrap}
  .brand{display:flex;align-items:center;justify-content:center;gap:6px;font-weight:800;text-align:center;line-height:1.05;z-index:2}
  .brand__dot{width:12px;height:12px;border-radius:50%;flex:none}
  .photo{position:absolute}
  .photo--crew{background:linear-gradient(135deg,#8a9399 0%,#6b7479 45%,#c07030 70%,#4b5358 100%)}
  .photo--cut{background:linear-gradient(160deg,#1b2a30 0%,#3f5c66 40%,#9b3fb5 70%,#161a1c 100%)}
  .photo--weld{background:radial-gradient(circle at 45% 75%,#f0b060 0%,#8a5a2a 12%,#2e3236 40%,#15181a 100%)}
  .contact{position:absolute;left:0;right:0;display:flex;align-items:center;justify-content:center;gap:10px;font-weight:700;font-size:13px;white-space:nowrap}
  .contact__item{display:flex;align-items:center;gap:4px}
  .contact svg{width:13px;height:13px;flex:none}
  .role-num{font-weight:800;font-style:italic;line-height:1}
  .role-box{position:absolute;background:var(--white);transform:skewX(-8deg)}
  .role-box span{display:block;transform:skewX(8deg);font-weight:800;font-style:italic;color:var(--ink);line-height:1.15}
  .perk-bar{position:absolute;background:var(--blue);height:7px}
</style>
</head>
<body>

<!-- Post A: black layout with photo strip -->
<section class="post post--a">
  <div class="abs headline" style="left:18px;top:12px;font-size:60px;color:var(--white)">WE’RE <span class="accent">HIRING</span></div>
  <div class="abs bold-it" style="right:17px;top:78px;font-size:26px;color:var(--white)">BOWEN BASIN BASED</div>
  <div class="abs brand" style="left:12px;top:92px;width:138px;height:70px;font-size:20px;color:var(--white)">
    <span class="brand__dot" style="background:var(--sky)"></span><span>KRT Plant Services</span>
  </div>
  <div class="abs role-num accent" style="left:156px;top:108px;font-size:54px">1</div>
  <div class="role-box" style="left:182px;top:116px;width:116px;height:41px;padding:6px 0 0 16px"><span style="font-size:12.5px">LEADING HAND<br>BOILERMAKER</span></div>
  <div class="abs role-num accent" style="left:304px;top:108px;font-size:54px">2</div>
  <div class="role-box" style="left:342px;top:116px;width:100px;height:41px;padding:6px 0 0 20px"><span style="font-size:12.5px">DRAGLINE<br>FITTER</span></div>

  <svg class="abs" style="left:0;top:174px" width="458" height="39" viewBox="0 0 458 39" aria-hidden="true">
    <defs><linearGradient id="stripA" x1="0" x2="1"><stop offset="0" stop-color="#0a6cff"/><stop offset="1" stop-color="#1ab8ff"/></linearGradient></defs>
    <rect width="458" height="39" fill="url(#stripA)"/>
    <polygon points="150,0 155,0 147,39 142,39" fill="#050505"/>
    <polygon points="310,0 315,0 307,39 302,39" fill="#050505"/>
  </svg>
  <div class="abs" style="left:12px;top:179px;display:flex;gap:6px;align-items:flex-end">
    <svg width="13" height="13" viewBox="0 0 13 13" aria-hidden="true" style="margin-bottom:3px"><rect x="1" y="2" width="10" height="10" fill="none" stroke="#fff" stroke-width="1.6"/><path d="M3 7l3 3 6-8" fill="none" stroke="#fff" stroke-width="1.8"/></svg>
    <div class="bold-it" style="font-size:12.5px;color:var(--white)">GREAT PAY +<br>LONG-TERM WORK</div>
  </div>
  <div class="abs" style="left:158px;top:179px;display:flex;gap:6px;align-items:flex-end">
    <svg width="13" height="13" viewBox="0 0 13 13" aria-hidden="true" style="margin-bottom:3px"><rect x="1" y="2" width="10" height="10" fill="none" stroke="#fff" stroke-width="1.6"/><path d="M3 7l3 3 6-8" fill="none" stroke="#fff" stroke-width="1.8"/></svg>
    <div class="bold-it" style="font-size:12.5px;color:var(--white)">DRAGLINE &amp; SHOVEL<br>MAINTENANCE</div>
  </div>
  <div class="abs" style="left:318px;top:179px;display:flex;gap:6px;align-items:flex-end">
    <svg width="13" height="13" viewBox="0 0 13 13" aria-hidden="true" style="margin-bottom:3px"><rect x="1" y="2" width="10" height="10" fill="none" stroke="#fff" stroke-width="1.6"/><path d="M3 7l3 3 6-8" fill="none" stroke="#fff" stroke-width="1.8"/></svg>
    <div class="bold-it" style="font-size:12.5px;color:var(--white)">LOCALLY OWNED<br>AND OPERATED</div>
  </div>

  <div class="abs" style="left:0;top:213px;width:458px;height:211px;background:var(--white)"></div>
  <div class="photo photo--crew" role="img" aria-label="Photo of crew working on dragline steel inside scaffolding" style="left:0;top:217px;width:138px;height:202px;clip-path:polygon(0 0,100% 0,73% 100%,0 100%)"></div>
  <div class="photo photo--cut" role="img" aria-label="Photo of plasma cutting machine working on steel plate" style="left:102px;top:217px;width:150px;height:202px;clip-path:polygon(26% 0,100% 0,74% 100%,0 100%)"></div>
  <div class="photo photo--weld" role="img" aria-label="Photo of boilermaker welding with sparks" style="left:215px;top:217px;width:243px;height:202px;clip-path:polygon(16% 0,100% 0,100% 100%,0 100%)"></div>

  <div class="contact" style="top:424px;height:34px;background:var(--black);color:var(--white);gap:10px">
    <span>CONTACT US</span>
    <span class="contact__item"><svg viewBox="0 0 14 14" aria-hidden="true"><circle cx="7" cy="7" r="7" fill="#1a7bff"/><path d="M4 4l6 2.5-2.3.8 1.8 2.2-1 .8-1.8-2.2-1.2 2z" fill="#fff"/></svg>KRTPLANTSERVICES.COM</span>
    <span class="contact__item"><svg viewBox="0 0 14 14" aria-hidden="true"><circle cx="7" cy="7" r="7" fill="#1a7bff"/><path d="M4.6 3.6l1.4 1.6-.8 1a5 5 0 002.6 2.6l1-.8 1.6 1.4-.8 1.2c-3 0-6.2-3.2-6.2-6.2z" fill="#fff"/></svg>0400 555 182</span>
  </div>
</section>

<!-- Post B: white layout with diagonal blue band -->
<section class="post post--b">
  <div class="abs" style="left:18px;top:10px;font-size:62px;font-weight:800;line-height:.92;letter-spacing:-1px;color:var(--black)">WE’RE<br>HIRING</div>
  <div class="abs bold-it" style="left:24px;top:121px;font-size:10.5px;color:var(--black)">BOWEN BASIN BASED</div>

  <div class="abs role-num" style="left:274px;top:16px;font-size:32px;color:var(--black)">1</div>
  <div class="perk-bar" style="left:267px;top:49px;width:24px;height:6px"></div>
  <div class="abs bold-it" style="left:304px;top:17px;font-size:19px;color:var(--black)">LEADING HAND<br>BOILERMAKER</div>
  <div class="abs role-num" style="left:274px;top:78px;font-size:32px;color:var(--black)">2</div>
  <div class="perk-bar" style="left:267px;top:111px;width:24px;height:6px"></div>
  <div class="abs bold-it" style="left:304px;top:79px;font-size:19px;color:var(--black)">DRAGLINE<br>FITTER</div>

  <svg class="abs" style="left:0;top:0" width="458" height="458" viewBox="0 0 458 458" aria-hidden="true">
    <defs><linearGradient id="bandB" x1="0" y1="1" x2="1" y2="0"><stop offset="0" stop-color="#0a6cff"/><stop offset="0.55" stop-color="#1a9dff"/><stop offset="1" stop-color="#14e6ff"/></linearGradient></defs>
    <polygon points="0,312 322,155 322,148 458,100 458,112 0,330" fill="#050505"/>
    <polygon points="0,330 458,112 458,458 0,458" fill="url(#bandB)"/>
    <polygon points="174,265 436,141 436,415 174,415" fill="#ffffff"/>
  </svg>
  <div class="photo photo--crew" role="img" aria-label="Photo of crew repairing dragline steel inside scaffolding" style="left:180px;top:149px;width:250px;height:261px;clip-path:polygon(0 45%,100% 0,100% 100%,0 100%)"></div>

  <div class="abs brand" style="left:12px;top:146px;width:160px;height:70px;font-size:24px;color:var(--ink)">
    <span class="brand__dot" style="background:var(--blue)"></span><span>KRT Plant Services</span>
  </div>

  <div class="abs bold-it" style="left:19px;top:333px;font-size:16px;color:var(--white)">GREAT PAY +<br>LONG-TERM WORK</div>
  <div class="abs bold-it" style="left:19px;top:380px;font-size:16px;color:var(--white)">LOCALLY OWNED<br>AND OPERATED</div>

  <div class="contact" style="top:426px;height:20px;color:var(--white);gap:11px">
    <span style="font-weight:600">CONTACT US</span>
    <span class="contact__item"><svg viewBox="0 0 14 14" aria-hidden="true"><circle cx="7" cy="7" r="7" fill="#050505"/><path d="M4 4l6 2.5-2.3.8 1.8 2.2-1 .8-1.8-2.2-1.2 2z" fill="#fff"/></svg>KRTPLANTSERVICES.COM</span>
    <span class="contact__item"><svg viewBox="0 0 14 14" aria-hidden="true"><circle cx="7" cy="7" r="7" fill="#050505"/><path d="M4.6 3.6l1.4 1.6-.8 1a5 5 0 002.6 2.6l1-.8 1.6 1.4-.8 1.2c-3 0-6.2-3.2-6.2-6.2z" fill="#fff"/></svg>0400 555 182</span>
  </div>
</section>

<!-- Post C: blue and white layout with hexagon photos -->
<section class="post post--c">
  <svg class="abs" style="left:0;top:0" width="458" height="458" viewBox="0 0 458 458" aria-hidden="true">
    <defs><linearGradient id="bgC" x1="0" y1="0" x2="1" y2="1"><stop offset="0" stop-color="#1a86ff"/><stop offset="1" stop-color="#0a3dff"/></linearGradient></defs>
    <rect width="458" height="458" fill="url(#bgC)"/>
    <polygon points="8,50 88,0 212,0 196,148 449,148 449,329 368,373 458,373 458,458 0,458 0,373 92,373 8,323 8,225 0,225 0,215 8,215" fill="#ffffff"/>
  </svg>
  <div class="abs brand" style="left:12px;top:30px;width:176px;height:88px;font-size:24px;color:var(--ink)">
    <span class="brand__dot" style="background:var(--blue)"></span><span>KRT Plant Services</span>
  </div>
  <div class="abs" style="left:226px;top:13px;font-size:58px;font-weight:800;font-style:italic;line-height:.96;letter-spacing:-1px;color:var(--white)">WE’RE<br>HIRING</div>
  <div class="abs bold-it" style="right:18px;top:127px;font-size:15px;color:var(--white)">Bowen Basin Based</div>

  <div class="abs bold-it" style="left:22px;top:158px;font-size:16.5px;line-height:1.3;color:var(--black)">GREAT PAY +<br>LONG-TERM WORK</div>
  <div class="abs role-num" style="left:206px;top:161px;font-size:24px;color:var(--black)">1</div>
  <div class="perk-bar" style="left:197px;top:186px;width:18px;height:5px"></div>
  <div class="abs" style="left:224px;top:161px;font-size:14.5px;font-style:italic;font-weight:600;line-height:1.2;color:var(--black)">LEADING HAND<br>BOILERMAKER</div>
  <div class="abs role-num" style="left:350px;top:161px;font-size:24px;color:var(--black)">2</div>
  <div class="perk-bar" style="left:341px;top:186px;width:18px;height:5px"></div>
  <div class="abs" style="left:369px;top:161px;font-size:14.5px;font-style:italic;font-weight:600;line-height:1.2;color:var(--black)">DRAGLINE<br>FITTER</div>

  <div class="photo" style="left:20px;top:206px;width:203px;height:165px;background:var(--blue-deep);clip-path:polygon(0 0,100% 0,100% 76%,50% 100%,0 76%)"></div>
  <div class="photo photo--crew" role="img" aria-label="Photo of crew working inside dragline scaffolding" style="left:24px;top:210px;width:195px;height:155px;clip-path:polygon(0 0,100% 0,100% 76%,50% 100%,0 76%)"></div>
  <div class="photo" style="left:236px;top:206px;width:202px;height:165px;background:var(--blue-deep);clip-path:polygon(0 0,100% 0,100% 76%,50% 100%,0 76%)"></div>
  <div class="photo photo--weld" role="img" aria-label="Photo of boilermaker welding with sparks" style="left:240px;top:210px;width:194px;height:155px;clip-path:polygon(0 0,100% 0,100% 76%,50% 100%,0 76%)"></div>
  <div class="photo" style="left:170px;top:322px;width:116px;height:94px;background:var(--blue-deep);clip-path:polygon(50% 0,100% 25%,100% 75%,50% 100%,0 75%,0 25%)"></div>
  <div class="photo photo--cut" role="img" aria-label="Photo of plasma cutting machine on steel plate" style="left:175px;top:327px;width:106px;height:84px;clip-path:polygon(50% 0,100% 25%,100% 75%,50% 100%,0 75%,0 25%)"></div>

  <div class="abs" style="left:25px;top:382px;font-size:12px;font-style:italic;line-height:1.25;color:var(--ink)">Dragline &amp; shovel<br>maintenance</div>
  <div class="abs" style="right:22px;top:382px;font-size:12px;font-style:italic;line-height:1.25;color:var(--ink)">Locally owned<br>and operated</div>

  <div class="contact" style="top:426px;height:20px;color:var(--ink);gap:11px">
    <span>CONTACT US</span>
    <span class="contact__item"><svg viewBox="0 0 14 14" aria-hidden="true"><circle cx="7" cy="7" r="7" fill="#1a7bff"/><path d="M4 4l6 2.5-2.3.8 1.8 2.2-1 .8-1.8-2.2-1.2 2z" fill="#fff"/></svg>KRTPLANTSERVICES.COM</span>
    <span class="contact__item"><svg viewBox="0 0 14 14" aria-hidden="true"><circle cx="7" cy="7" r="7" fill="#1a7bff"/><path d="M4.6 3.6l1.4 1.6-.8 1a5 5 0 002.6 2.6l1-.8 1.6 1.4-.8 1.2c-3 0-6.2-3.2-6.2-6.2z" fill="#fff"/></svg>0400 555 182</span>
  </div>
</section>

<!-- Post D: dark workshop layout with hexagon photo -->
<section class="post post--d">
  <div class="photo" role="img" aria-label="Dark workshop background photo of dragline steelwork" style="inset:0;background:linear-gradient(160deg,#2a2d31 0%,#141618 50%,#24272a 100%)"></div>
  <div class="abs headline" style="left:18px;top:12px;font-size:60px;color:var(--white)">WE’RE <span class="accent">HIRING</span></div>
  <div class="abs bold-it" style="right:18px;top:69px;font-size:21px;color:var(--white)">BOWEN BASIN BASED</div>
  <div class="abs brand" style="left:8px;top:100px;width:200px;height:100px;font-size:26px;color:var(--white)">
    <span class="brand__dot" style="background:var(--sky)"></span><span>KRT Plant Services</span>
  </div>

  <div class="abs role-num accent" style="left:221px;top:101px;font-size:40px">1</div>
  <div class="role-box" style="left:242px;top:107px;width:88px;height:30px;padding:4px 0 0 10px"><span style="font-size:9.5px;font-weight:700">LEADING HAND<br>BOILERMAKER</span></div>
  <div class="abs role-num accent" style="left:336px;top:101px;font-size:40px">2</div>
  <div class="role-box" style="left:361px;top:107px;width:76px;height:30px;padding:4px 0 0 16px"><span style="font-size:9.5px;font-weight:700">DRAGLINE<br>FITTER</span></div>

  <div class="abs bold-it" style="left:328px;top:148px;font-size:17px;color:var(--white)">GREAT PAY +</div>
  <div class="abs" style="left:328px;top:167px;font-size:9.5px;font-style:italic;font-weight:700;color:var(--white)">long-term work</div>
  <div class="perk-bar" style="left:440px;top:155px;width:18px;height:9px"></div>

  <div class="perk-bar" style="left:0;top:255px;width:17px;height:9px"></div>
  <div class="abs bold-it" style="left:21px;top:251px;font-size:17px;color:var(--white)">DRAGLINE<br>&amp; SHOVEL</div>
  <div class="abs" style="left:21px;top:290px;font-size:9.5px;font-style:italic;font-weight:700;color:var(--white)">maintenance</div>
  <div class="perk-bar" style="left:0;top:312px;width:17px;height:9px"></div>
  <div class="abs bold-it" style="left:21px;top:308px;font-size:17px;color:var(--white)">LOCALLY<br>OWNED</div>
  <div class="abs" style="left:21px;top:347px;font-size:9.5px;font-style:italic;font-weight:700;color:var(--white)">and operated</div>

  <div class="photo photo--weld" role="img" aria-label="Photo of boilermaker welding with sparks" style="left:116px;top:163px;width:317px;height:253px;clip-path:polygon(50% 0,100% 36%,100% 64%,50% 100%,0 64%,0 36%)"></div>
  <svg class="abs" style="left:0;top:0" width="458" height="458" viewBox="0 0 458 458" aria-hidden="true">
    <polygon points="274,163 433,255 433,325 274,416 116,325 116,255" fill="none" stroke="#19a8ff" stroke-width="4"/>
  </svg>

  <div class="contact" style="top:423px;height:20px;color:var(--white);gap:11px">
    <span>CONTACT US</span>
    <span class="contact__item"><svg viewBox="0 0 14 14" aria-hidden="true"><circle cx="7" cy="7" r="7" fill="#1a7bff"/><path d="M4 4l6 2.5-2.3.8 1.8 2.2-1 .8-1.8-2.2-1.2 2z" fill="#fff"/></svg>KRTPLANTSERVICES.COM</span>
    <span class="contact__item"><svg viewBox="0 0 14 14" aria-hidden="true"><circle cx="7" cy="7" r="7" fill="#1a7bff"/><path d="M4.6 3.6l1.4 1.6-.8 1a5 5 0 002.6 2.6l1-.8 1.6 1.4-.8 1.2c-3 0-6.2-3.2-6.2-6.2z" fill="#fff"/></svg>0400 555 182</span>
  </div>
</section>

</body>
</html>
```